Jewelry Website needs fully functional Website (Wordpress + Ecommerce))

The Wordpress site will have to be fully functional with an Ecommerce integration and will need to be SEO optimized.
We would like to have an Journal integration to the website so viewers can see updates posted (see halvorkeene.ca)
We sell real fine gold and diamond jewelry. The website should have an elegant, modern, professional and high end look. It will be the decision maker for people to order their jewelry from the website, therefore it should be easily navigated by users.
Target Audience are women from 16-50 years old.
Attached is a Logo of our brand that will command how the website should look.
For inspiration purposes here is a list of websites that we like:
halvorkeene.ca/
http://www.mirolaquin.com/
Get creative and show us your talent!
Target Market(s)
The target market are women ages 16-50.
Industry/Entity Type
Jewelry
Look and feel
Each slider illustrates characteristics of the customer's brand and the style your logo design should communicate.

```html
<!DOCTYPE html>
<html lang="en">
<head>
<meta charset="utf-8">
<title>Selene Marlow Jewelry</title>
<link rel="stylesheet" href="https://fonts.googleapis.com/css2?family=Oswald:wght@300;400;500&family=Lato:wght@300;400;700&family=Cormorant+Garamond:wght@400;500&display=swap">
<style>
:root{
  --ink:#1c1c1c;
  --black:#0b0b0b;
  --white:#ffffff;
  --paper:#f7f7f7;
  --line:#d9d9d9;
  --muted:#8a8a8a;
  --accent:#e3174c;
  --price:#c21e2a;
  --dark-panel:#2e2f33;
}
*{margin:0;padding:0;box-sizing:border-box}
html,body{width:1200px;height:3985px;overflow:hidden;background:var(--white)}
body{position:relative;font-family:"Lato",sans-serif;color:var(--ink)}
.abs{position:absolute}
.photo{position:absolute}
.heading{font-family:"Oswald",sans-serif;text-transform:uppercase;font-weight:400;letter-spacing:1px}
.btn{position:absolute;display:flex;align-items:center;justify-content:center;font-family:"Lato",sans-serif;font-weight:700;font-size:11px;letter-spacing:1.5px;text-transform:uppercase}
.btn-light{background:var(--white);color:var(--ink)}
.btn-dark{background:var(--ink);color:var(--white)}
.btn-outline{border:2px solid var(--ink);color:var(--ink);background:var(--white)}

/* header */
.utility-nav{top:8px;left:0;width:1200px;display:flex;justify-content:center;gap:34px;font-size:11px;color:var(--muted);letter-spacing:.5px}
.utility-nav .current{color:var(--ink);border-bottom:1px solid var(--ink)}
.brand{display:flex;align-items:center;gap:10px;font-family:"Cormorant Garamond",serif;font-size:26px;color:var(--ink);letter-spacing:1px}
.brand-dot{width:44px;height:44px;border:1.5px solid var(--ink);border-radius:50%}
.header-brand{top:42px;left:0;width:1200px;justify-content:center}
.search{top:52px;left:18px;width:170px;height:28px;border:1px solid var(--line);font-size:10px;color:var(--muted);padding:8px 10px;letter-spacing:1px}
.cart{top:52px;right:18px;width:180px;height:28px;border:1px solid var(--ink);font-size:10px;letter-spacing:1px;display:flex;align-items:center;justify-content:center;gap:8px}
.main-nav{top:112px;left:0;width:1200px;display:flex;justify-content:center;gap:48px;font-size:12px;color:#555}
.header-rule{top:100px;left:0;width:1200px;height:1px;background:#ececec}

/* hero */
.hero{top:155px;left:0;width:1200px;height:620px;background:var(--black)}
.hero-photo{left:560px;top:0;width:640px;height:620px;background:linear-gradient(100deg,#0b0b0b 0%,#2b211c 25%,#6b4a3b 55%,#3a2a22 100%)}
.hero-kicker{left:120px;top:228px;color:var(--white);font-size:17px;letter-spacing:2px}
.hero-title{left:120px;top:255px;color:var(--white);font-size:42px;font-family:"Cormorant Garamond",serif;letter-spacing:1px}
.hero-rule{left:120px;top:318px;width:390px;height:1px;background:#555}
.hero-text{left:120px;top:330px;width:380px;color:#aaa;font-size:10px;line-height:15px}
.arrow{width:26px;height:26px}

/* tiles */
.mens{top:788px;left:0;width:731px;height:497px;background:linear-gradient(180deg,#2d2d30 0%,#c77a20 40%,#e08c22 60%,#3a3a3d 100%)}
.mens-kicker{top:150px;left:0;width:731px;text-align:center;color:var(--white);font-size:24px}
.mens-title{top:180px;left:0;width:731px;text-align:center;color:var(--white);font-size:46px;font-family:"Cormorant Garamond",serif}
.rings{top:788px;left:745px;width:455px;height:497px;background:linear-gradient(135deg,#9c6a56 0%,#d7a891 45%,#b98470 70%,#6d4638 100%)}
.rings-text{left:30px;top:360px;color:var(--white);font-size:34px;line-height:38px;font-family:"Cormorant Garamond",serif;text-transform:uppercase}

/* lookbook */
.lookbook{top:1298px;left:0;width:1200px;height:554px;background:var(--black)}
.lookbook-photo{left:600px;top:0;width:600px;height:554px;background:linear-gradient(100deg,#0b0b0b 0%,#3b2a1e 25%,#a87a55 55%,#d8b48a 80%,#6e4c33 100%)}
.lookbook-kicker{left:133px;top:122px;color:var(--white);font-size:17px;letter-spacing:1px}
.lookbook-title{left:133px;top:150px;color:var(--white);font-size:66px;font-family:"Cormorant Garamond",serif;letter-spacing:2px}
.product-card{left:965px;top:164px;width:143px;height:243px;background:var(--white);box-shadow:0 4px 14px rgba(0,0,0,.35)}
.product-photo{left:14px;top:14px;width:115px;height:115px;background:radial-gradient(circle,#e9e6df 0%,#a7a198 55%,#f4f4f4 80%)}
.product-name{left:14px;top:140px;font-size:10px;font-weight:700;letter-spacing:1px}
.product-price{left:14px;top:158px;font-size:15px;color:var(--price);font-weight:700}
.product-note{left:14px;top:184px;width:115px;font-size:8px;color:var(--muted);line-height:12px}

/* row 4 */
.video{top:1865px;left:0;width:607px;height:629px;background:linear-gradient(160deg,#5b5551 0%,#9a8d85 35%,#c7a796 55%,#4b3e3a 100%)}
.video-title{left:40px;top:520px;color:var(--white);font-size:52px;font-family:"Cormorant Garamond",serif}
.play{left:160px;top:455px}
.pendants{top:1865px;left:620px;width:580px;height:315px;background:var(--white);border-bottom:1px solid #ececec}
.pendant-photo{left:50px;top:20px;width:250px;height:270px;background:radial-gradient(circle at 50% 55%,#e7e7e9 0%,#ffffff 55%)}
.pendants-number{right:25px;top:22px;font-size:22px;color:var(--ink)}
.pendants-title{right:25px;top:48px;font-size:24px;text-align:right;line-height:26px}
.pendants-text{right:25px;top:112px;width:205px;font-size:9px;line-height:13px;color:#555;text-align:left}
.earrings{top:2193px;left:620px;width:580px;height:301px;background:#f3f3f3}
.earrings-number{left:45px;top:24px;font-size:22px}
.earrings-title{left:45px;top:48px;font-size:24px}
.earrings-text{left:45px;top:90px;width:220px;font-size:9px;line-height:13px;color:#555}
.earring-photo{left:300px;top:30px;width:240px;height:250px;background:radial-gradient(ellipse at 50% 50%,#d7dadf 0%,#f3f3f3 60%)}

/* row 5 */
.testimonials{top:2512px;left:0;width:735px;height:500px;background:linear-gradient(90deg,#111 0%,#2c2d31 35%,#3a3b40 100%)}
.testimonial-title{left:0;top:118px;width:735px;text-align:center;color:var(--white);font-size:30px;font-family:"Cormorant Garamond",serif;letter-spacing:2px}
.testimonial-rule{left:330px;top:164px;width:75px;height:1px;background:#888}
.testimonial-text{left:180px;top:180px;width:375px;text-align:center;color:#bbb;font-size:10px;line-height:16px}
.testimonial-more{left:0;top:270px;width:735px;text-align:center;color:#ddd;font-size:9px;letter-spacing:1px}
.sale{top:2512px;left:748px;width:452px;height:500px;background:var(--accent);color:var(--white);text-align:center}
.sale-kicker{top:60px;left:0;width:452px;font-size:18px;letter-spacing:2px}
.sale-title{top:90px;left:0;width:452px;font-size:128px;line-height:130px;font-family:"Oswald",sans-serif;font-weight:300;letter-spacing:4px}
.sale-sub{top:240px;left:0;width:452px;font-size:32px;letter-spacing:4px;font-family:"Oswald",sans-serif;font-weight:300}
.sale-note{top:448px;left:0;width:452px;font-size:9px;letter-spacing:2px;opacity:.85}

/* appointment */
.appointment-title{top:3096px;left:0;width:1200px;text-align:center;font-family:"Cormorant Garamond",serif;font-size:34px;letter-spacing:2px}
.appointment-sub{top:3148px;left:0;width:1200px;text-align:center;font-size:12px;letter-spacing:2px}
.appointment-rule{top:3172px;left:560px;width:80px;height:1px;background:var(--ink)}
.field{position:absolute;height:44px;border:1px solid var(--line);font-size:12px;color:#777;padding:14px 14px}
.submit{top:3487px;left:520px;width:160px;height:44px}

/* footer */
.footer-brand{top:3560px;left:0;width:1200px;justify-content:center;font-size:40px}
.footer-brand .brand-dot{width:70px;height:70px}
.footer-col{width:300px;text-align:center}
.footer-col h3{font-family:"Lato",sans-serif;font-size:12px;letter-spacing:2px;font-weight:700}
.footer-col p{font-size:12px;color:#555;margin-top:14px}
.footer-rule{top:3730px;width:300px;height:1px;background:var(--line)}
.social{top:3920px;left:0;width:1200px;display:flex;justify-content:center;gap:60px;font-size:10px;font-weight:700;letter-spacing:1.5px}
.to-top{left:570px;top:3955px;width:60px;height:60px;border-radius:50%;background:var(--ink)}
</style>
</head>
<body>

<header>
  <nav class="abs utility-nav" aria-label="Utility">
    <span class="current">About</span><span>Blog</span><span>Shop</span><span>Stories</span><span>Wishlist</span>
  </nav>
  <div class="abs search">SEARCH</div>
  <div class="abs brand header-brand"><span class="brand-dot"></span><span>Selene Marlow</span></div>
  <div class="abs cart">
    <svg width="12" height="12" viewBox="0 0 12 12"><path d="M1 3h10l-1 8H2z" fill="none" stroke="#1c1c1c"/><path d="M4 3V2a2 2 0 0 1 4 0v1" fill="none" stroke="#1c1c1c"/></svg>
    MY SHOPPING BAG (0)
  </div>
  <div class="abs header-rule"></div>
  <nav class="abs main-nav" aria-label="Collections">
    <span>Engagement Rings</span><span>Wedding Rings</span><span>Bracelets</span><span>Custom Design</span><span>Earrings</span><span>Pendants</span>
  </nav>
</header>

<section class="abs hero">
  <div class="photo hero-photo" role="img" aria-label="Model with dark curly hair wearing a diamond ring"></div>
  <div class="abs heading hero-kicker">Introducing our first</div>
  <div class="abs hero-title">WEDDING COLLECTION</div>
  <div class="abs hero-rule"></div>
  <div class="abs hero-text">Timeless bands in fine gold and diamonds, crafted for the day you say yes.</div>
  <div class="btn btn-light" style="left:120px;top:370px;width:88px;height:26px">Take a look</div>
  <svg class="abs arrow" style="left:10px;top:300px" viewBox="0 0 26 26"><path d="M2 13h18M14 7l6 6-6 6M2 4v18" fill="none" stroke="#fff" stroke-width="2"/></svg>
  <svg class="abs arrow" style="right:10px;top:300px" viewBox="0 0 26 26"><path d="M24 13H6M12 7l-6 6 6 6M24 4v18" fill="none" stroke="#fff" stroke-width="2"/></svg>
</section>

<section class="abs mens" role="img" aria-label="Man in an orange jacket checking his phone">
  <div class="abs heading mens-kicker">New men's</div>
  <div class="abs mens-title">COLLECTION</div>
  <div class="btn btn-light" style="left:320px;top:262px;width:90px;height:26px">Take a look</div>
</section>
<section class="abs rings" role="img" aria-label="Hand wearing a diamond engagement ring">
  <div class="abs rings-text">New rings<br>arrivals</div>
</section>

<section class="abs lookbook">
  <div class="photo lookbook-photo" role="img" aria-label="Blonde model with hand to face showing a ring"></div>
  <div class="abs heading lookbook-kicker">Engagement | Wedding 2014</div>
  <div class="abs lookbook-title">LOOK BOOK</div>
  <div class="btn btn-light" style="left:133px;top:355px;width:90px;height:26px">Take a look</div>
  <div class="abs product-card">
    <div class="photo product-photo" role="img" aria-label="Emerald halo ring"></div>
    <div class="abs product-name">HALO RING</div>
    <div class="abs product-price">$1,950</div>
    <div class="abs product-note">Emerald centre stone in a pavé diamond halo.</div>
  </div>
</section>

<section class="abs video" role="img" aria-label="Hands holding a ruby ring, video still">
  <svg class="abs play" width="34" height="34" viewBox="0 0 34 34"><circle cx="17" cy="17" r="16" fill="none" stroke="#fff" stroke-width="2"/><path d="M13 10l11 7-11 7z" fill="#fff"/></svg>
  <div class="abs video-title">PLAY VIDEO</div>
</section>

<section class="abs pendants">
  <div class="photo pendant-photo" role="img" aria-label="Round diamond halo pendant on a fine chain"></div>
  <div class="abs heading pendants-number">03</div>
  <div class="abs heading pendants-title">Pendants<br>models</div>
  <div class="abs pendants-text"><b>STARTING FROM $799</b><br>Soft halos and solitaires set on delicate chains for every neckline.</div>
  <div class="btn btn-dark" style="right:25px;top:226px;width:90px;height:26px">Take a look</div>
</section>
<section class="abs earrings">
  <div class="abs heading earrings-number">04</div>
  <div class="abs heading earrings-title">Earrings</div>
  <div class="abs earrings-text"><b>STARTING FROM $450</b><br>Diamond hoops and studs in white and yellow gold, made to order.</div>
  <div class="btn btn-dark" style="left:45px;top:230px;width:86px;height:26px">Shop now</div>
  <div class="photo earring-photo" role="img" aria-label="Pair of diamond hoop earrings"></div>
</section>

<section class="abs testimonials" role="img" aria-label="Man in a dark suit, portrait background">
  <div class="abs testimonial-title">TESTIMONIALS</div>
  <div class="abs testimonial-rule"></div>
  <div class="abs testimonial-text">“The ring was even more beautiful in person. The team guided me through every detail and delivered it right on time. She said yes the moment she saw it.”</div>
  <div class="abs testimonial-more">READ MORE</div>
</section>
<section class="abs sale">
  <div class="abs sale-kicker">SECRET</div>
  <div class="abs sale-title">SALE</div>
  <div class="abs sale-sub">UP TO 50% OFF</div>
  <div class="abs sale-note">ONE WEEK · SELECT PIECES ONLY</div>
</section>

<section>
  <h2 class="abs appointment-title" style="font-weight:400">MAKE AN APPOINTMENT</h2>
  <div class="abs appointment-sub">COME VISIT US</div>
  <div class="abs appointment-rule"></div>
  <div class="field" style="left:244px;top:3205px;width:346px">Name</div>
  <div class="field" style="left:606px;top:3205px;width:346px">Surname</div>
  <div class="field" style="left:244px;top:3280px;width:346px">Email</div>
  <div class="field" style="left:606px;top:3280px;width:346px">Phone Number</div>
  <div class="field" style="left:244px;top:3355px;width:708px;height:92px">Comments</div>
  <div class="btn btn-dark submit">Submit</div>
</section>

<footer>
  <div class="abs brand footer-brand"><span class="brand-dot"></span><span>Selene Marlow</span></div>
  <div class="abs footer-rule" style="left:240px"></div>
  <div class="abs footer-rule" style="left:660px"></div>
  <div class="abs footer-col" style="left:240px;top:3745px"><h3>CONTACT</h3><p>Don't hesitate to say hi!</p></div>
  <div class="abs footer-col" style="left:660px;top:3745px"><h3>PRESSKIT</h3><p>Download the media kit</p></div>
  <div class="btn btn-outline" style="left:315px;top:3820px;width:150px;height:30px">Write to us</div>
  <div class="btn btn-outline" style="left:735px;top:3820px;width:150px;height:30px">Press</div>
  <nav class="abs social" aria-label="Social"><span>LOOKBOOK</span><span>JOURNAL</span><span>UPDATES</span><span>STORIES</span></nav>
  <div class="abs to-top"></div>
  <svg class="abs" style="left:592px;top:3962px" width="16" height="10" viewBox="0 0 16 10"><path d="M2 8l6-6 6 6" fill="none" stroke="#fff" stroke-width="2"/></svg>
</footer>

</body>
</html>
```